Dentistry

Dentist's personal business card. No logo needed. The card shoul deliver the massage of reliability, professionalism, experience.
Please ad the full brief of the project: down the line it says: the winning look should be precise and pristine NO pictures of Teeth, smiles, instruments etc.

The details to be desplaid are:
Dr. Lev Oranbury
Doctor of Dental Surgery
PHD
Web. Www.droranbury.example
Email. Lev@droranbury.example
Tel 07700900318
Surgery address. 27Bfernwick road London SE4 7QX UK
62 Harlow Crescent London EC3V 9PD. Uk

Industry/Entity Type

Massage

Requirements
Should not have
• Logo, teeth, smile any sort of instruments.

```html
<!DOCTYPE html>
<html lang="en">
<head>
<meta charset="utf-8">
<title>Dr. Lev Oranbury – Business Card</title>
<link rel="stylesheet" href="https://fonts.googleapis.com/css2?family=Jost:wght@500;600&family=Open+Sans:wght@400;600&display=swap">
<style>
  :root {
    --blue: #1c86ef;
    --blue-deep: #1677dc;
    --ink: #1f2a33;
    --ink-soft: #3a3f44;
    --white: #ffffff;
    --backdrop: #eceef1;
    --field-line: #0e5fb4;
  }
  * { box-sizing: border-box; margin: 0; padding: 0; }
  html, body { width: 1200px; height: 800px; overflow: hidden; }
  body {
    background: var(--backdrop);
    display: flex;
    align-items: center;
    justify-content: center;
    gap: 50px;
    font-family: "Open Sans", Arial, sans-serif;
  }
  .card {
    position: relative;
    width: 540px;
    height: 310px;
    box-shadow: 0 6px 18px rgba(0,0,0,.18);
    overflow: hidden;
  }

  /* Front */
  .card-front { background: var(--white); }
  .edge-bar {
    position: absolute;
    width: 15px;
    background: var(--blue);
  }
  .edge-bar--left { left: 0; top: 38px; height: 214px; }
  .edge-bar--right { right: 0; top: 20px; height: 200px; }
  .front-identity {
    position: absolute;
    left: 0; right: 0; top: 124px;
    text-align: center;
    font-family: "Jost", "Futura", sans-serif;
  }
  .front-name {
    color: var(--blue);
    font-weight: 600;
    font-size: 27px;
    letter-spacing: .3px;
    line-height: 1.1;
  }
  .front-title {
    color: var(--ink-soft);
    font-weight: 500;
    font-size: 18px;
    margin-top: 4px;
    padding-left: 40px;
  }

  /* Back */
  .card-back { background: var(--blue); color: var(--white); }
  .back-header {
    position: absolute;
    top: 24px; left: 24px; right: 20px;
    display: flex;
  }
  .back-identity { width: 232px; padding-left: 6px; }
  .back-name { font-size: 19px; font-weight: 600; line-height: 1.2; }
  .back-title { color: var(--ink); font-size: 13.5px; margin-top: 1px; padding-left: 26px; }
  .back-address { color: var(--ink); font-size: 10.5px; margin-top: 1px; }
  .divider { width: 2px; height: 84px; background: var(--ink); margin: 0 28px 0 10px; }
  .contact-list { list-style: none; font-size: 11.5px; }
  .contact-list li { display: flex; align-items: center; gap: 7px; height: 21px; }
  .contact-list svg { width: 13px; height: 13px; fill: none; stroke: var(--ink); stroke-width: 1.6; flex: none; }
  .contact-list svg .solid { fill: var(--ink); stroke: none; }

  .appointment-heading {
    position: absolute;
    top: 124px; left: 0; right: 0;
    text-align: center;
    font-family: "Jost", "Futura", sans-serif;
    font-weight: 600;
    font-size: 30px;
    letter-spacing: 2.5px;
  }
  .field-row {
    position: absolute;
    left: 20px; right: 20px;
    display: flex;
    align-items: center;
    font-size: 16px;
    color: var(--ink);
  }
  .field-row--name { top: 190px; }
  .field-row--when { top: 246px; }
  .field-box {
    height: 32px;
    background: var(--white);
    border-bottom: 2px solid var(--field-line);
    box-shadow: inset 0 1px 2px rgba(0,0,0,.12);
  }
  .field-row--name .field-box { flex: 1; margin-left: 8px; }
  .field-box--date { width: 180px; margin-left: 14px; }
  .field-label--time { margin-left: 26px; }
  .field-box--time { flex: 1; margin-left: 14px; }
</style>
</head>
<body>

  <section class="card card-front" aria-label="Business card front">
    <span class="edge-bar edge-bar--left"></span>
    <span class="edge-bar edge-bar--right"></span>
    <div class="front-identity">
      <h1 class="front-name">DR. LEV ORANBURY, Ph.D.</h1>
      <p class="front-title">Doctor of Dental Surgery</p>
    </div>
  </section>

  <section class="card card-back" aria-label="Business card back">
    <header class="back-header">
      <div class="back-identity">
        <h2 class="back-name">DR. LEV ORANBURY, Ph.D.</h2>
        <p class="back-title">Doctor of Dental Surgery</p>
        <p class="back-address">27Bfernwick road London SE4 7QX UK</p>
      </div>
      <span class="divider"></span>
      <ul class="contact-list">
        <li>
          <svg viewBox="0 0 16 16" aria-hidden="true"><path class="solid" d="M3.5 1.5l2.5 0 1 3.5-1.8 1.2a8 8 0 0 0 4.6 4.6L11 9l3.5 1v2.5c0 1-1 2-2 2C6.5 14.5 1.5 9.5 1.5 3.5c0-1 1-2 2-2z"/></svg>
          07 700900318
        </li>
        <li>
          <svg viewBox="0 0 16 16" aria-hidden="true"><rect x="1.5" y="3.5" width="13" height="9" rx="1"/><path d="M1.5 4l6.5 5 6.5-5"/></svg>
          Lev@droranbury.example
        </li>
        <li>
          <svg viewBox="0 0 16 16" aria-hidden="true"><path class="solid" d="M8 1.5L.8 8h2.2v6.5h3.8v-4h2.4v4H13V8h2.2z"/></svg>
          62 Harlow Crescent London EC3V 9PD. Uk
        </li>
        <li>
          <svg viewBox="0 0 16 16" aria-hidden="true"><circle cx="8" cy="8" r="6.5"/><ellipse cx="8" cy="8" rx="2.8" ry="6.5"/><path d="M1.5 8h13M2.5 4.8h11M2.5 11.2h11"/></svg>
          www.droranbury.example
        </li>
      </ul>
    </header>

    <h3 class="appointment-heading">APPOINTMENT</h3>

    <div class="field-row field-row--name">
      <span class="field-label">Name</span>
      <span class="field-box"></span>
    </div>
    <div class="field-row field-row--when">
      <span class="field-label">Date</span>
      <span class="field-box field-box--date"></span>
      <span class="field-label field-label--time">Time</span>
      <span class="field-box field-box--time"></span>
    </div>
  </section>

</body>
</html>
```